BrookhavenLLC

Real Estate Investment. Buy/Sell house/investment . Trustworthy,Reliable, and friendly

Industry/Entity Type

Real Estate

Contact Information for Business Card

Brookhaven@mailbox-example.com
808-555-0143
Linnea-Joy Patterson

```html
<!DOCTYPE html>
<html lang="en">
<head>
<meta charset="UTF-8">
<title>Brookhaven LLC — Business Card</title>
<link rel="stylesheet" href="https://fonts.googleapis.com/css2?family=Marcellus&family=Montserrat:wght@500&family=Open+Sans:wght@400;600&display=swap">
<style>
  :root {
    --backdrop: #b3b3b3;
    --card-white: #ffffff;
    --brand-green: #3ab54a;
    --band-green: #2fae44;
    --ink-black: #111111;
    --panel-black: #141414;
    --panel-black-edge: #0a0a0a;
    --contact-white: #f2f2f2;
  }
  * { margin: 0; padding: 0; box-sizing: border-box; }
  html, body {
    width: 1200px;
    height: 900px;
    overflow: hidden;
    background: var(--backdrop);
  }
  .canvas {
    position: relative;
    width: 1200px;
    height: 900px;
    display: flex;
    align-items: center;
    justify-content: center;
  }
  .business-card {
    width: 880px;
    height: 500px;
    border-radius: 34px;
    overflow: hidden;
    background: var(--card-white);
    display: flex;
    flex-direction: column;
    box-shadow: 0 18px 40px rgba(0, 0, 0, 0.22);
  }
  .card-brand {
    height: 272px;
    display: flex;
    align-items: center;
    padding-left: 52px;
    gap: 26px;
  }
  .brand-square {
    width: 150px;
    height: 150px;
    background: var(--brand-green);
    flex-shrink: 0;
  }
  .brand-text {
    display: flex;
    flex-direction: column;
    gap: 10px;
  }
  .brand-name {
    font-family: "Marcellus", serif;
    font-size: 62px;
    line-height: 1;
    color: var(--brand-green);
    letter-spacing: 1px;
    text-transform: uppercase;
  }
  .brand-tagline {
    font-family: "Montserrat", sans-serif;
    font-weight: 500;
    font-size: 22px;
    letter-spacing: 5px;
    color: var(--ink-black);
    text-transform: uppercase;
  }
  .card-band {
    height: 16px;
    background: var(--band-green);
  }
  .card-contact {
    flex: 1;
    background: linear-gradient(180deg, var(--panel-black) 0%, var(--panel-black-edge) 100%);
    display: flex;
    flex-direction: column;
    align-items: center;
    justify-content: center;
    padding-bottom: 26px;
    text-align: center;
  }
  .contact-name {
    font-family: "Open Sans", sans-serif;
    font-weight: 600;
    font-size: 38px;
    color: var(--brand-green);
    margin-bottom: 12px;
  }
  .contact-phone {
    font-family: "Open Sans", sans-serif;
    font-size: 32px;
    letter-spacing: 3px;
    color: var(--contact-white);
    line-height: 1.2;
  }
  .contact-email {
    font-family: "Open Sans", sans-serif;
    font-size: 26px;
    letter-spacing: 1.5px;
    color: var(--contact-white);
    line-height: 1.3;
  }
</style>
</head>
<body>
  <main class="canvas">
    <article class="business-card">
      <header class="card-brand">
        <div class="brand-square"></div>
        <div class="brand-text">
          <h1 class="brand-name">Brookhaven LLC</h1>
          <p class="brand-tagline">Real Estate Investment</p>
        </div>
      </header>
      <div class="card-band"></div>
      <section class="card-contact">
        <p class="contact-name">Linnea-Joy Patterson</p>
        <p class="contact-phone">808-555-0143</p>
        <p class="contact-email">Brookhaven@mailbox-example.com</p>
      </section>
    </article>
  </main>
</body>
</html>
```